Sunny Paths and joy Business card

I have a logo, but will like a business card design. Is for a travel agency in Mexico. We focus in family experiences.

I will liek some thing different and unique, from the traditional business card, something to get remmeber for.

Business card information:

Leandro T. Ocampo
leandro@sunnypathsjoy.example

Alameda 482, 3 piso
Col. Tlalpizco
Mexico, D.F. 07320

office: (55) 5000-0142
mobile: (55) 9000-0187

www.sunnypathsjoy.example
@sunnypjoy
blog: sunnypathsandjoy.blogsite.example
facebook: SunnyPathsAndJoy

```html
<!DOCTYPE html>
<html lang="es">
<head>
<meta charset="utf-8">
<title>Sunny Paths and joy – Business card</title>
<link rel="stylesheet" href="https://fonts.googleapis.com/css2?family=Open+Sans:wght@400;700;800&display=swap">
<style>
  :root {
    --stage: #2a2a2a;
    --card-white: #ffffff;
    --brand-blue: #1a5fbf;
    --brand-navy: #1d4a8c;
    --sky-light: #c9e2f5;
    --sky-mid: #8cbce6;
    --text-light: #ffffff;
  }
  * { box-sizing: border-box; margin: 0; padding: 0; }
  html, body {
    width: 1200px;
    height: 900px;
    overflow: hidden;
    background: var(--stage);
    font-family: "Open Sans", Arial, sans-serif;
  }
  .canvas {
    position: relative;
    width: 1200px;
    height: 900px;
  }
  .card {
    position: absolute;
    width: 640px;
    height: 380px;
    overflow: hidden;
    box-shadow: 0 10px 28px rgba(0,0,0,0.55);
  }

  /* Front */
  .card-front {
    left: 90px;
    top: 60px;
    background: var(--card-white);
  }
  .brand-illustration {
    position: absolute;
    left: 210px;
    top: 40px;
    width: 220px;
    height: 160px;
    border-radius: 50%;
    background: radial-gradient(ellipse at center, var(--sky-mid) 0%, var(--sky-light) 70%, rgba(201,226,245,0) 100%);
  }
  .brand-name {
    position: absolute;
    left: 0;
    right: 0;
    top: 210px;
    text-align: center;
    font-weight: 800;
    font-size: 40px;
    line-height: 1.1;
    color: var(--brand-navy);
  }
  .front-band {
    position: absolute;
    left: 0;
    right: 0;
    bottom: 0;
    height: 78px;
  }
  .front-band .rule {
    position: absolute;
    left: 0;
    right: 0;
    top: 0;
    height: 4px;
    background: var(--brand-blue);
  }
  .front-band .strip {
    position: absolute;
    left: 0;
    right: 0;
    top: 12px;
    bottom: 0;
    background: var(--brand-blue);
    display: flex;
    align-items: center;
    justify-content: center;
  }
  .front-band .website {
    color: var(--text-light);
    font-size: 19px;
    letter-spacing: 0.28em;
  }

  /* Back */
  .card-back {
    left: 470px;
    top: 460px;
    background: var(--brand-blue);
  }
  .back-pattern {
    position: absolute;
    inset: 0;
    background: radial-gradient(circle at 75% 70%, rgba(140,188,230,0.25) 0%, rgba(140,188,230,0) 60%);
  }
  .contact {
    position: absolute;
    inset: 0;
    display: flex;
    flex-direction: column;
    align-items: center;
    justify-content: center;
    color: var(--text-light);
    font-size: 17px;
    line-height: 1.2;
    text-align: center;
  }
  .contact .group + .group { margin-top: 22px; }
</style>
</head>
<body>
<main class="canvas">
  <section class="card card-front" aria-label="Card front">
    <div class="brand-illustration" role="img" aria-label="Illustration of a smiling blue cartoon airplane carrying two waving children over a pale blue sky"></div>
    <div class="brand-name">Sunny Paths and joy</div>
    <div class="front-band">
      <div class="rule"></div>
      <div class="strip"><span class="website">www.sunnypathsandjoy.example</span></div>
    </div>
  </section>

  <section class="card card-back" aria-label="Card back">
    <div class="back-pattern" role="img" aria-label="Pattern of soft outlined clouds on blue"></div>
    <div class="contact">
      <div class="group">
        <p class="name">Leandro T. Ocampo</p>
        <p class="email">leandro@sunnypathsjoy.example</p>
      </div>
      <div class="group">
        <p>Alameda 482, 3 piso</p>
        <p>Col. Tlalpizco</p>
        <p>Mexico, D.F. 07320</p>
      </div>
      <div class="group">
        <p>office: (55) 5000-0142</p>
        <p>mobile: (55) 9000-0187</p>
      </div>
      <div class="group">
        <p>www.sunnypathsjoy.example</p>
        <p>@sunnypjoy</p>
        <p>blog: sunnypathsandjoy.blogsite.example</p>
        <p>facebook: SunnyPathsAndJoy</p>
      </div>
    </div>
  </section>
</main>
</body>
</html>
```